New Print Material Needed for Renovation Company

We are looking to update our current Print Material to reflect the current process we offer to our clients. A lot of the information is also outdated along with many of the photos that are currently being used. We are a renovation company that specializes in residential and commercial renovations and custom builds.This project is MULTIPLE pages. We will pay the chosen designer an extra fee for the designing 3-4 additional pages that are similar to the chosen design. Attached is our current Print Material. We are hoping to update the look of them and some of the messaging. Our current company colors are white, blue and light grey and it will remain that way.

Industry/Entity Type

Construction Company

Font styles to use
Sans Serif

Colors
3176b5
ffffff

Requirements
Must have
• Easy to explain the process
• Easy to read and understand let alone
• Easy to navigate
Nice to have
• As much creativity as possible
Should not have
• no confusing text
• no confusing layout

```html
<!DOCTYPE html>
<html lang="en">
<head>
<meta charset="utf-8">
<title>Master Builder Timeline</title>
<link rel="stylesheet" href="https://fonts.googleapis.com/css2?family=Fira+Sans:wght@800&family=Montserrat:wght@600;800&family=Source+Sans+3:wght@400;600&display=swap">
<style>
  :root {
    --blue: #1a64a3;
    --blue-dark: #14568e;
    --ink: #222326;
    --tab-ink: #5f6166;
    --paper: #ffffff;
    --grey-light: #f4f5f6;
    --grey-mid: #d9dbde;
    --body-ink: #1b1b1b;
  }
  * { margin: 0; padding: 0; box-sizing: border-box; }
  html, body { width: 1200px; height: 927px; overflow: hidden; background: var(--paper); }
  .sheet { position: relative; width: 1200px; height: 927px; background: var(--paper); }

  .emblem { position: absolute; left: 68px; top: 40px; width: 158px; height: 158px; border-radius: 50%; background: var(--blue); }

  .title {
    position: absolute; left: 256px; top: 96px;
    font-family: "Fira Sans", sans-serif; font-weight: 800;
    font-size: 43px; letter-spacing: 0.5px; color: var(--ink); white-space: nowrap;
  }

  .brand {
    position: absolute; left: 901px; top: 57px; width: 229px; height: 128px;
    background: var(--blue); display: flex; align-items: center; justify-content: center; gap: 10px;
  }
  .brand-mark { width: 14px; height: 14px; background: var(--paper); }
  .brand-name { font-family: "Source Sans 3", sans-serif; font-weight: 600; font-size: 16px; color: var(--paper); line-height: 1.15; }

  .column { position: absolute; top: 0; width: 372px; height: 927px; }
  .column--design { left: 0; }
  .column--plan { left: 372px; }
  .column--build { left: 744px; }

  .spine {
    position: absolute; width: 6px;
    background: linear-gradient(90deg, rgba(0,0,0,0), rgba(0,0,0,0.12), rgba(0,0,0,0));
  }

  .phase { position: absolute; left: 41px; top: 267px; width: 196px; height: 80px; }
  .phase svg { position: absolute; left: 0; top: 0; }
  .phase-name {
    position: absolute; left: 0; top: 18px; width: 150px; text-align: center;
    font-family: "Montserrat", sans-serif; font-weight: 800; font-size: 19px; color: var(--tab-ink); letter-spacing: 0.5px;
  }
  .phase-letter {
    position: absolute; left: 180px; top: 20px; width: 30px; text-align: center;
    font-family: "Montserrat", sans-serif; font-weight: 800; font-size: 18px; color: var(--paper);
  }

  .step { position: absolute; left: 0; width: 372px; height: 130px; }
  .step-card { position: absolute; left: 60px; top: 0; }
  .step-number {
    position: absolute; left: 60px; top: 2px; width: 82px; text-align: right;
    font-family: "Montserrat", sans-serif; font-weight: 800; font-size: 44px; color: var(--blue); line-height: 56px;
  }
  .step-text { position: absolute; left: 188px; top: -4px; width: 200px; text-align: center; }
  .step-title {
    font-family: "Montserrat", sans-serif; font-weight: 600; font-size: 14.5px;
    color: var(--blue); letter-spacing: 0.6px; white-space: nowrap; line-height: 18px;
  }
  .step-duration { font-family: "Source Sans 3", sans-serif; font-size: 12.5px; color: var(--blue); line-height: 15px; }
  .step-body {
    margin-top: 9px; text-align: left; padding-left: 8px;
    font-family: "Source Sans 3", sans-serif; font-weight: 600; font-size: 8.3px; line-height: 10.5px; color: var(--body-ink);
  }
</style>
</head>
<body>
<main class="sheet">
  <div class="emblem" role="img" aria-label="Round blue seal emblem with crossed tools"></div>
  <h1 class="title">MASTER BUILDER TIMELINE</h1>
  <div class="brand"><span class="brand-mark"></span><span class="brand-name">Harbourline<br>Renovations</span></div>

  <svg width="0" height="0" aria-hidden="true" style="position:absolute">
    <defs>
      <linearGradient id="paperFold" x1="0" x2="1" y1="0" y2="0">
        <stop offset="0" stop-color="#ffffff"/>
        <stop offset="1" stop-color="#d6d8db"/>
      </linearGradient>
      <linearGradient id="dropShade" x1="0" x2="0" y1="0" y2="1">
        <stop offset="0" stop-color="#000" stop-opacity="0.22"/>
        <stop offset="1" stop-color="#000" stop-opacity="0"/>
      </linearGradient>
    </defs>
  </svg>

  <!-- DESIGN -->
  <section class="column column--design">
    <div class="spine" style="left:62px;top:242px;height:138px"></div>
    <div class="spine" style="left:60px;top:412px;height:130px"></div>
    <div class="spine" style="left:60px;top:575px;height:130px"></div>
    <div class="spine" style="left:64px;top:738px;height:130px"></div>
    <div class="phase">
      <svg width="200" height="80"><path d="M0 60 L128 58 L185 68 L60 74 Z" fill="url(#dropShade)"/><path d="M2 5 L120 1 L142 30 L118 60 L2 62 Q-4 62 0 66 Q2 72 18 72 L2 72 Z" fill="url(#paperFold)"/><path d="M116 6 L168 6 L194 31 L168 56 L111 56 L138 31 Z" fill="var(--blue)"/></svg>
      <div class="phase-name">DESIGN</div><div class="phase-letter">A</div>
    </div>
    <article class="step" style="top:444px">
      <svg class="step-card" width="125" height="95"><path d="M4 60 L92 60 L110 78 L10 72 Z" fill="url(#dropShade)"/><path d="M0 0 L86 0 L100 30 L86 61 L0 61 Z" fill="url(#paperFold)"/><path d="M94 8 L104 8 L118 31 L104 54 L94 54 L108 31 Z" fill="var(--blue)"/></svg>
      <div class="step-number">1</div>
      <div class="step-text"><div class="step-title">INITIAL DESIGN MEETING</div><div class="step-duration">1-2 weeks</div><p class="step-body">The first step of design process is to confirm the design concept you have envisioned</p></div>
    </article>
    <article class="step" style="top:606px">
      <svg class="step-card" width="125" height="95"><path d="M4 60 L92 60 L110 78 L10 72 Z" fill="url(#dropShade)"/><path d="M0 0 L86 0 L100 30 L86 61 L0 61 Z" fill="url(#paperFold)"/><path d="M94 8 L104 8 L118 31 L104 54 L94 54 L108 31 Z" fill="var(--blue)"/></svg>
      <div class="step-number">2</div>
      <div class="step-text"><div class="step-title">SECOND DESIGN MEETING</div><div class="step-duration">1-2 weeks</div><p class="step-body">Our designers work directly with you to ensure the measurements line up with your design ideas</p></div>
    </article>
    <article class="step" style="top:770px">
      <svg class="step-card" width="125" height="95" style="left:65px"><path d="M4 60 L92 60 L110 78 L10 72 Z" fill="url(#dropShade)"/><path d="M0 0 L86 0 L100 30 L86 61 L0 61 Z" fill="url(#paperFold)"/><path d="M94 8 L104 8 L118 31 L104 54 L94 54 L108 31 Z" fill="var(--blue)"/></svg>
      <div class="step-number" style="left:65px">3</div>
      <div class="step-text" style="left:183px"><div class="step-title">FINAL DESIGN MEETING</div><div class="step-duration">1-3 weeks</div><p class="step-body">Any last minute or final revisions will be completed with in three days of this meeting</p></div>
    </article>
  </section>

  <!-- PLAN -->
  <section class="column column--plan">
    <div class="spine" style="left:62px;top:242px;height:138px"></div>
    <div class="spine" style="left:69px;top:412px;height:130px"></div>
    <div class="spine" style="left:69px;top:575px;height:130px"></div>
    <div class="spine" style="left:59px;top:738px;height:130px"></div>
    <div class="phase">
      <svg width="200" height="80"><path d="M0 60 L128 58 L185 68 L60 74 Z" fill="url(#dropShade)"/><path d="M2 5 L120 1 L142 30 L118 60 L2 62 Q-4 62 0 66 Q2 72 18 72 L2 72 Z" fill="url(#paperFold)"/><path d="M116 6 L168 6 L194 31 L168 56 L111 56 L138 31 Z" fill="var(--blue)"/></svg>
      <div class="phase-name" style="left:10px">PLAN</div><div class="phase-letter">B</div>
    </div>
    <article class="step" style="top:444px">
      <svg class="step-card" width="125" height="95" style="left:70px"><path d="M4 60 L92 60 L110 78 L10 72 Z" fill="url(#dropShade)"/><path d="M0 0 L86 0 L100 30 L86 61 L0 61 Z" fill="url(#paperFold)"/><path d="M94 8 L104 8 L118 31 L104 54 L94 54 L108 31 Z" fill="var(--blue)"/></svg>
      <div class="step-number" style="left:70px">4</div>
      <div class="step-text" style="top:2px;left:200px"><div class="step-title">MATERIAL SELECTION</div><div class="step-duration">1-4 weeks</div><p class="step-body">Our material selection coordinator will work with you to ensure all the right materials</p></div>
    </article>
    <article class="step" style="top:606px">
      <svg class="step-card" width="125" height="95" style="left:70px"><path d="M4 60 L92 60 L110 78 L10 72 Z" fill="url(#dropShade)"/><path d="M0 0 L86 0 L100 30 L86 61 L0 61 Z" fill="url(#paperFold)"/><path d="M94 8 L104 8 L118 31 L104 54 L94 54 L108 31 Z" fill="var(--blue)"/></svg>
      <div class="step-number" style="left:70px">5</div>
      <div class="step-text" style="left:202px"><div class="step-title">ENGINEERING DRAWING</div><div class="step-duration">2-4 weeks</div><p class="step-body">The final permit designs will be sent to engineers to ensure structral integrity</p></div>
    </article>
    <article class="step" style="top:770px">
      <svg class="step-card" width="125" height="95" style="left:61px"><path d="M4 60 L92 60 L110 78 L10 72 Z" fill="url(#dropShade)"/><path d="M0 0 L86 0 L100 30 L86 61 L0 61 Z" fill="url(#paperFold)"/><path d="M94 8 L104 8 L118 31 L104 54 L94 54 L108 31 Z" fill="var(--blue)"/></svg>
      <div class="step-number" style="left:52px">6</div>
      <div class="step-text" style="left:205px;top:-6px"><div class="step-title">BUILDING PERMIT PLANS</div><div class="step-duration">2-25 weeks</div><p class="step-body">Permit drawings will begin once the build has been signed and inital payments has been made</p></div>
    </article>
  </section>

  <!-- BUILD -->
  <section class="column column--build">
    <div class="spine" style="left:62px;top:242px;height:138px"></div>
    <div class="spine" style="left:67px;top:412px;height:130px"></div>
    <div class="spine" style="left:71px;top:575px;height:130px"></div>
    <div class="spine" style="left:67px;top:738px;height:130px"></div>
    <div class="phase">
      <svg width="200" height="80"><path d="M0 60 L128 58 L185 68 L60 74 Z" fill="url(#dropShade)"/><path d="M2 5 L120 1 L142 30 L118 60 L2 62 Q-4 62 0 66 Q2 72 18 72 L2 72 Z" fill="url(#paperFold)"/><path d="M116 6 L168 6 L194 31 L168 56 L111 56 L138 31 Z" fill="var(--blue)"/></svg>
      <div class="phase-name" style="left:20px;top:15px">BUILD</div><div class="phase-letter" style="top:18px">C</div>
    </div>
    <article class="step" style="top:444px">
      <svg class="step-card" width="125" height="95" style="left:68px"><path d="M4 60 L92 60 L110 78 L10 72 Z" fill="url(#dropShade)"/><path d="M0 0 L86 0 L100 30 L86 61 L0 61 Z" fill="url(#paperFold)"/><path d="M94 8 L104 8 L118 31 L104 54 L94 54 L108 31 Z" fill="var(--blue)"/></svg>
      <div class="step-number" style="left:60px">7</div>
      <div class="step-text" style="top:2px;left:206px"><div class="step-title">MATERIAL FINALIZATION</div><div class="step-duration">2-4 weeks</div><p class="step-body">A lead designer will finalize any revisions you may have for your material selection</p></div>
    </article>
    <article class="step" style="top:604px">
      <svg class="step-card" width="125" height="95" style="left:72px"><path d="M4 60 L92 60 L110 78 L10 72 Z" fill="url(#dropShade)"/><path d="M0 0 L86 0 L100 30 L86 61 L0 61 Z" fill="url(#paperFold)"/><path d="M94 8 L104 8 L118 31 L104 54 L94 54 L108 31 Z" fill="var(--blue)"/></svg>
      <div class="step-number" style="left:64px">8</div>
      <div class="step-text" style="top:6px;left:206px"><div class="step-title">CONSTRUCTION PLANS</div><div class="step-duration">2-6 weeks</div><p class="step-body">The drawing will be updated within 24 hours once the permit have been approved and recieved</p></div>
    </article>
    <article class="step" style="top:770px">
      <svg class="step-card" width="125" height="95" style="left:68px"><path d="M4 60 L92 60 L110 78 L10 72 Z" fill="url(#dropShade)"/><path d="M0 0 L86 0 L100 30 L86 61 L0 61 Z" fill="url(#paperFold)"/><path d="M94 8 L104 8 L118 31 L104 54 L94 54 L108 31 Z" fill="var(--blue)"/></svg>
      <div class="step-number" style="left:56px">9</div>
      <div class="step-text" style="top:-2px;left:206px"><div class="step-title">SCHEDULING</div><div class="step-duration">2-4 weeks</div><p class="step-body">All the designs , dates, permits have been completed.The project is ready to underway</p></div>
    </article>
  </section>
</main>
</body>
</html>
```